Schulungen und Brandschutzdienstleistungen
Zielgruppe
Wir sind im vorbeugenden und organisatorischen Brandschutz tätig. Unsere Zielgruppe sind Firmen die Unterstützung, Beratung und die Schulung Ihrer Mitarbeiter beötigen.
Aufgabenstellung
Vorgaben ergeben sich aus dem Design der Homepage und dem pdf Upload (Beispiel des letzten Flyers).
Es sollen die Schulungsleistungen wie Brandschutzhelfer, Erste Hilfe und Unterweisungen hervorgehoben werden. Weiterhin sollen unsere Dienstleistungen, insbesondere der externe Brandschutzbeauftragte, aufgezeigt werden.
Schön währe auf der letzten Seite ein Anmeldeformular für die Schulungen.
Texte und Logo dürfen gerne verwendet werden.
Die Flyer soll zusammen mit einem Anschreiben in eine DIN lang Briefumschlag passen.

```html
<!DOCTYPE html>
<html lang="de">
<head>
<meta charset="utf-8">
<title>Brandschutz Wolters – Flyer 2017</title>
<link href="https://fonts.googleapis.com/css2?family=Open+Sans:wght@300;400;500;600;700;800&display=swap" rel="stylesheet">
<style>
:root{
  --red:#8e0d0d;
  --red-text:#9a1010;
  --white:#ffffff;
  --ink:#3a3a3a;
  --stage:#d6d6d6;
}
*{box-sizing:border-box;margin:0;padding:0}
html,body{width:935px;height:1200px;overflow:hidden;background:var(--stage)}
body{font-family:"Open Sans",Arial,sans-serif;position:relative}
.sheet{position:absolute;left:129px;width:708px;height:506px;background:var(--white);box-shadow:3px 4px 6px rgba(0,0,0,.35);overflow:hidden}
.sheet--outside{top:59px}
.sheet--inside{top:612px;height:505px}
.abs{position:absolute}
.photo{position:absolute}

/* outside: about panel */
.about{left:0;top:0;width:233px;height:506px;background:var(--red)}
.about__photo{left:0;top:3px;width:233px;height:200px;background:linear-gradient(160deg,#cfd3d6,#7d8790 55%,#2c3440)}
.about__band{left:0;top:200px;width:233px;height:26px;background:linear-gradient(90deg,#e2e2e2,#bfbfbf)}
.about__title{left:10px;top:201px;font-size:21px;font-weight:700;color:var(--red-text)}
.about__text{left:16px;top:243px;width:205px;font-size:8.4px;line-height:11.9px;color:var(--white);font-weight:300;hyphens:auto}
.about__text p{margin-bottom:11.9px}
.about__sign{font-weight:400}

/* outside: form panel */
.form{left:233px;top:0;width:231px;height:506px}
.form__title{left:12px;top:12px;font-size:16.5px;font-weight:700;color:var(--red-text);letter-spacing:.2px}
.form__row{position:absolute;left:12px;width:210px;display:flex;align-items:flex-end;font-size:8.4px;color:var(--ink)}
.form__row span{white-space:nowrap;margin-right:3px}
.form__row i{flex:1;border-bottom:1px solid var(--red-text);height:1px}
.form__check{left:9px;top:226px;width:11px;height:11px;border:1.2px solid var(--red-text)}
.form__checktext{left:26px;top:224px;font-size:8.4px;line-height:15px;color:var(--red-text)}
.form__date{left:12px;top:277px;width:210px;font-size:8.4px;color:var(--red-text);display:flex;align-items:flex-end}
.form__date i{flex:1;border-bottom:1px solid var(--red-text);margin-left:4px}
.form__sig{top:336px;border-top:1px solid var(--red-text);font-size:8.4px;color:var(--ink);text-align:center;padding-top:2px}
.form__reach{left:0;top:392px;width:231px;text-align:center;font-size:11.5px;font-weight:600;color:var(--red-text)}
.contact{left:0;top:412px;width:231px;height:94px;background:var(--red)}
.contact__col{position:absolute;width:115px;text-align:center;font-size:6.8px;line-height:10px;color:#f1d6d6;font-weight:300}
.contact__col b{font-weight:700;color:var(--white)}

/* outside: cover panel */
.cover{left:464px;top:0;width:244px;height:506px;background:var(--red)}
.cover__brand{left:10px;top:8px;font-size:28px;line-height:38px;font-weight:800;color:var(--white);letter-spacing:1px}
.cover__photo{left:2px;top:89px;width:242px;height:376px;background:linear-gradient(135deg,#e9e9e9,#b9bcc0 40%,#d8342b 62%,#c51f1a)}
.cover__ribbon{left:14px;top:303px;width:230px;height:56px;background:var(--red);transform:rotate(-8deg);transform-origin:left top;display:flex;flex-direction:column;justify-content:center;padding-left:14px;box-shadow:2px 3px 4px rgba(0,0,0,.3)}
.cover__ribbon span{font-size:17px;line-height:21px;font-weight:800;color:var(--white);letter-spacing:.6px}
.cover__year{left:0;top:468px;width:244px;text-align:center;font-size:35px;line-height:36px;font-weight:800;color:var(--white)}

/* inside */
.inside__bg{position:absolute;left:0;top:0}
.helper__title{left:12px;top:11px;font-size:16.5px;font-weight:600;color:var(--white)}
.txt{position:absolute;font-size:8.4px;line-height:11.9px;font-weight:300;text-align:justify;hyphens:auto}
.txt--light{color:var(--white)}
.txt--dark{color:var(--ink)}
.txt p{margin-bottom:11.9px}
.caption{left:12px;top:286px;font-size:8.4px;line-height:11.5px;color:var(--red-text);font-weight:500}
.course__title{left:256px;top:106px;width:260px;text-align:center;font-size:16px;line-height:22px;font-weight:700;color:var(--red-text)}
.small{position:absolute;font-size:6.8px;line-height:9.8px;color:var(--ink);font-weight:300}
.small b{color:var(--red-text);font-weight:600}
.termine__title{left:236px;top:425px;font-size:8.6px;color:var(--red-text);font-weight:500}
.termin{position:absolute;font-size:6.8px;line-height:8.5px;color:var(--white);text-align:center;width:100px;font-weight:300}
.termin b{font-weight:500}
.officer__title{left:540px;top:7px;width:156px;text-align:right;font-size:16px;line-height:21px;font-weight:600;color:var(--white)}
.officer__band{left:480px;top:258px;width:215px;text-align:right;font-size:8.4px;line-height:11.9px;color:var(--white);font-weight:500}
</style>
</head>
<body>

<section class="sheet sheet--outside">
  <div class="abs about">
    <div class="photo about__photo" role="img" aria-label="Porträtfoto des Inhabers"></div>
    <div class="abs about__band"></div>
    <h2 class="abs about__title">ÜBER UNS:</h2>
    <div class="abs about__text">
      <p>Durch meine knapp 20-jährige Berufserfahrung als aktiver Feuerwehrbeamter wird mir die zerstörerische Kraft eines Feuers und der damit verbundenen Schäden täglich aufs Neue vorgeführt.</p>
      <p>Aufgrund meiner langjährigen Erfahrung im Brandschutz möchte ich mit meinem Unternehmen mit Ihnen gemeinsam die richtigen und vor allem sinnvollen präventiven Brandschutzmaßnahmen ergreifen, um größere Schäden zu verhindern.</p>
      <p>Mein Ziel ist die Aufklärung, Beratung sowie das Training vor Ort und damit der Schutz von Leib, Leben und Sachwerten.</p>
      <p>Mit Ihnen gemeinsam plane ich aus der Praxis für die Praxis.</p>
      <p class="about__sign">Markus Wolters</p>
    </div>
  </div>

  <div class="abs form">
    <h2 class="abs form__title">ANMELDEFORMULAR:</h2>
    <div class="form__row" style="top:46px"><span>Name:</span><i></i></div>
    <div class="form__row" style="top:74px"><span>Vorname:</span><i></i></div>
    <div class="form__row" style="top:102px"><span>Straße:</span><i></i></div>
    <div class="form__row" style="top:131px"><span>PLZ, Wohnort:</span><i></i></div>
    <div class="form__row" style="top:162px"><span>Telefon:</span><i></i></div>
    <div class="form__row" style="top:189px"><span>E-Mail:</span><i></i></div>
    <div class="abs form__check"></div>
    <div class="abs form__checktext">Ich möchte an der Schulung zum<br>Brandschutzhelfer teilnehmen.</div>
    <div class="abs form__date">Als Termin bevorzuge ich den:<i></i></div>
    <div class="abs form__sig" style="left:12px;width:77px">Datum</div>
    <div class="abs form__sig" style="left:113px;width:109px">Unterschrift</div>
    <div class="abs form__reach">So erreichen Sie uns:</div>
    <div class="abs contact">
      <div class="contact__col" style="left:0;top:10px"><b>Brandschutz Wolters</b><br>Lindenweg 12<br>12345 Talbrück<br><br>(01234) 555 0147<br>info@brandschutz-wolters.de</div>
      <div class="contact__col" style="left:113px;top:10px">Besuchen Sie uns im Web:<br><br><b>www.brandschutz-wolters.de</b><br><br>Seminare und Schulungen<br>auch online buchbar.</div>
    </div>
  </div>

  <div class="abs cover">
    <h1 class="abs cover__brand">BRANDSCHUTZ<br>WOLTERS</h1>
    <div class="photo cover__photo" role="img" aria-label="Foto eines roten Feuerlöschers auf einem Kasten mit Feuerlöscher-Schild"></div>
    <div class="abs cover__ribbon"><span>SCHULUNGEN UND</span><span>DIENSTLEISTUNGEN</span></div>
    <div class="abs cover__year">2017</div>
  </div>
</section>

<section class="sheet sheet--inside">
  <svg class="inside__bg" width="708" height="505" viewBox="0 0 708 505">
    <defs>
      <linearGradient id="fire" x1="0" y1="0" x2="1" y2="1"><stop offset="0" stop-color="#5b5a5c"/><stop offset=".45" stop-color="#e9a23a"/><stop offset="1" stop-color="#f6d27a"/></linearGradient>
      <linearGradient id="group" x1="0" y1="0" x2="1" y2="0"><stop offset="0" stop-color="#d8c2b3"/><stop offset=".5" stop-color="#ece6e0"/><stop offset="1" stop-color="#c7ced6"/></linearGradient>
      <linearGradient id="detector" x1="0" y1="0" x2="1" y2="1"><stop offset="0" stop-color="#f2f2f2"/><stop offset="1" stop-color="#bdbdbd"/></linearGradient>
    </defs>
    <polygon points="0,0 277,0 255,180 0,180" fill="var(--red)"/>
    <polygon points="0,180 270,180 262,317 0,317" fill="url(#fire)" role="img" aria-label="Foto einer Person, die mit einem Feuerlöscher einen Brand löscht"/>
    <polygon points="0,281 213,281 209,310 0,310" fill="var(--white)"/>
    <polygon points="213,281 220,281 216,310 209,310" fill="var(--red)"/>
    <polygon points="0,317 228,317 215,440 443,440 440,505 0,505" fill="var(--red)"/>
    <polygon points="277,0 534,0 515,173 255,173" fill="url(#group)" role="img" aria-label="Foto einer lächelnden Schulungsgruppe"/>
    <polygon points="262,106 522,106 515,173 255,173" fill="rgba(255,255,255,.72)"/>
    <polygon points="534,0 708,0 708,52 528,52" fill="var(--red)"/>
    <polygon points="476,251 708,251 708,296 470,296" fill="var(--red)"/>
    <polygon points="453,405 708,405 708,411 453,411" fill="var(--red)"/>
    <polygon points="453,411 708,411 708,505 440,505" fill="url(#detector)" role="img" aria-label="Foto eines Rauchmelders auf einem Merkblatt"/>
  </svg>

  <h2 class="abs helper__title">Brandschutzhelfer</h2>
  <div class="txt txt--light" style="left:12px;top:37px;width:245px">
    <p>Nach dem Arbeitsschutzgesetz (§10 ArbSchG – Erste Hilfe und sonstige Notfallmaßnahmen) und den Vorschriften der Berufsgenossenschaften ist jeder Arbeitgeber verpflichtet, in angemessenen Zeitabständen seine Mitarbeiter für das richtige Verhalten im Brandfall zu schulen.</p>
    <p>Seit 01.01.2013 ist die Arbeitsstätten - Regel ASR A2.2 - Maßnahmen gegen Brände, gültig. Darin wird die Zahl der Brandschutzhelfer auf mindestens 5% der Arbeitnehmer festgelegt. Die Versicherer haben dies größtenteils zu Ihren Bedingungen gemacht.</p>
  </div>
  <div class="abs caption">Sind Ihre Mitarbeiter ausreichend für den<br>Brand vorbereitet?</div>
  <div class="txt txt--light" style="left:12px;top:330px;width:200px">
    <p>Was nützt Ihnen die Anschaffung gesetzlich vorgeschriebener Feuerlöscher oder Selbsthilfeeinrichtungen, wenn im Ernstfall keiner mit den Geräten umgehen kann. Laut einer Umfrage eines Fachverbands für Brandschutz haben 69% aller Befragten noch nie an einer Brandschutzschulung aktiv teilgenommen</p>
    <p style="font-weight:400">Daher veranstalten wir regelmäßig Seminare für Brandschutzhelfer.</p>
  </div>

  <div class="abs course__title">Brandschutzhelfer<br>Ausbildung nach DGUV<br>Information 205-023</div>
  <div class="txt txt--dark" style="left:281px;top:187px;width:208px">Die Ausbildung umfasst ca. drei Unterrichtseinheiten a`45 Minuten. Die Zeitdauer für die Praxis nach Abschnitt 2.2 der DGUV Information 205-023 hängt von der Gruppengröße ab. Jeder Teilnehmer bekommt ausreichend Übungszeit zur Verfügung gestellt.</div>
  <div class="small" style="left:266px;top:267px;width:200px">Teilnahmegebühr: 95,00 EURO zzgl. 19%MwSt.<br>Inklusive Tagungsgetränke (Frischer Bohnenkaffee und Tee sowie Softdrinks) und Teilnehmerunterlagen.</div>
  <div class="small" style="left:258px;top:311px"><b>Hinweise:</b><br>Festes Schuhwerk und angepasste Kleidung<br>für Praxisübungen im Freien.<br>Gültiges Ausweisdokument.</div>
  <div class="small" style="left:244px;top:363px"><b>Tagungsort:</b><br>Haus am Ufer<br>Seeweg 8<br>12345 Talbrück<br><br>Raum Seeblick</div>
  <div class="abs termine__title">TERMINE 2017</div>
  <div class="termin" style="left:215px;top:446px"><b>Mittwoch, 27.04.2016</b><br>von 09:00 - 13:00 Uhr</div>
  <div class="termin" style="left:331px;top:446px"><b>Mittwoch, 08.06.2016</b><br>von 09:00 - 13:00 Uhr</div>
  <div class="termin" style="left:215px;top:471px"><b>Mittwoch, 18.05.2016</b><br>von 09:00 - 13:00 Uhr</div>
  <div class="termin" style="left:331px;top:471px"><b>Mittwoch, 29.06.2016</b><br>von 09:00 - 13:00 Uhr</div>

  <h2 class="abs officer__title">Brandschutz-<br>beauftragter</h2>
  <div class="txt txt--dark" style="left:530px;top:56px;width:164px">
    <p>Für den Brandschutz in Betrieben sind aufgrund besonderer Rechtsvorschriften, behördlichen Auflagen oder Gefährdungsbeurteilungen Brandschutzbeauftragte erforderlich, die durch ihre qualifizierte Ausbildung dem Unternehmer/Arbeitgeber als zentraler Partner für brandschutzrelevante Themen zur Verfügung stehen.</p>
    <p>Je nach Unternehmensgröße ist es effizienter und wirtschaftlicher, diese Aufgabe einem erfahrenen, externen Brandschutzbeauftragten zu übertragen um einen ganzheitlichen Brandschutz im Unternehmen gewährleisten zu können.</p>
  </div>
  <div class="abs officer__band">Wir übernehmen für Sie als Unternehmer oder Betreiber einer Immobilie die Funktion des Brandschutzbeauftragten.</div>
  <div class="txt txt--dark" style="left:500px;top:306px;width:194px">
    <p>Nutzen Sie die Vorteile von aktuellem Fachwissen und umfangreichen Erfahrungen im vorbeugenden, organisatorischen und abwehrenden Brandschutz.</p>
    <p>Wir würden uns sehr freuen, wenn wir die Aufgabe des externen Brandschutzbeauftragen für Sie übernehmen dürfen.</p>
  </div>
</section>

</body>
</html>
```